Progressive business consultancy seeking innovative and clever powerpoint design

Were looking for a PowerPoint design for our Melbourne based business consulting company, Vantora.

About Us:
Based in Melbourne, Australia, Vantora is a management consulting organisation that partners with their clients to lead the execution of strategic process and system improvement initiatives.

Vantora offers business advisory services in Project Management, Business Process Management, Change Management, Business Analysis and Business Intelligence. Vantora combines hands on delivery with coaching in best practice methodologies and approaches to build our clients capabilities ensuring their ongoing success in project implementations.

Vantora has extensive experience across a wide range of industries. We specialise in assisting organisations across the accounting, legal, financial services and health sectors.

Our core purpose is to help businesses in the middle market navigate transformational change through clear and focused execution and enablement.

www.vantora.com.au
@vantora_hq

What we're looking for:
A PowerPoint template consisting of:
- a front/cover page with hero image (attached)
- a contents page
- a divider page (for different segments of the slide deck)
- a standard PowerPoint content page
- a blank PowerPoint page. (still Vantora themed)

The Vantora colours are white and blue (RGB:0/86/162 and
CMYK 97/73/4/0)

All slides should have the Vantora logo (attached) and a professional, almost corporate, (but not boring) theme that is consistent across all slides. The design should reflect our focus on the "e" in vantora, which is what we're really about - "e"xecution and "e"nablement of change.

I've attached a PNG file of our word template which shows the focus on the "e" as a watermark on the document as well as the font files if required.

Let me know if you need any further information or design specifics.

Thanks,

Marjorie
(on behalf of Desmond)
Updates

Project Deadline Extended
Reason: Hi Designers, We have received some really great designs. Thanks for taking the time to make your submissions. We have decided to extend the deadline as we need some more time to review and consult other colleagues on the great submissions we have received. We are also hoping we might get some additional submissions over the weekend. We would also like enough time to provide feedback on all the submissions received. Thanks for helping us out with some really creative work. Desmond @vantora_hq

Project Deadline Extended
Reason: Hi designers, thanks for taking the time to submit your designs. We have some really great submissions. We are going to have to extend our deadline again as we just haven't had the chance to review and provide feedback on all the designs. We will be closing this project off on Tuesday March 17. Thanks Desmond @vantora_hq

Target Market(s)

C-Level executives (CEO,COO,CIO) at professional services firms (Accounting and Legal), not for profit organisations and financial services firms.

Industry/Entity Type

Management Consulting

Font styles to use
Serif
Other font styles liked:
• Calibri or attached fonts

Requirements
Must have
• A PowerPoint template consisting of:
• 1) a front/cover page with hero image (attached)
• 2) a contents page
• 3) a divider page (for different segments of the slide deck)
• 4) a standard PowerPoint content page
• 5) a blank PowerPoint page. (still Vantora themed)
• 6) Two content
• 7) Comparison
• 8) Table
• 9) Picture column
• 10) Chevron
• The Vantora colours are white and blue (RGB:0/86/162 and
• CMYK 97/73/4/0)

```html
<!DOCTYPE html>
<html lang="en">
<head>
<meta charset="utf-8">
<title>Vantora – Picture Column Slides</title>
<link rel="stylesheet" href="https://fonts.googleapis.com/css2?family=Abel&family=Saira+Condensed:wght@700&display=swap">
<style>
  :root {
    --brand-blue: #0b57a6;
    --brand-blue-dark: #0a4283;
    --ink: #111111;
    --body-text: #1e1e1e;
    --paper: #ffffff;
    --footer-band: #e3e7f1;
    --backdrop: #eceef2;
  }
  * { margin: 0; padding: 0; box-sizing: border-box; }
  html, body { width: 849px; height: 1200px; overflow: hidden; }
  body {
    background: var(--backdrop);
    font-family: "Abel", sans-serif;
    position: relative;
  }
  .slide {
    position: absolute;
    width: 704px;
    height: 528px;
    background: var(--paper);
    overflow: hidden;
    box-shadow: 0 2px 8px rgba(0,0,0,0.12);
  }
  .slide--first { left: 72px; top: 73px; }
  .slide--second { left: 83px; top: 615px; width: 698px; height: 523px; }

  .slide__header {
    position: absolute; left: 0; top: 0;
    width: 100%; height: 88px;
    background: var(--brand-blue);
  }
  .brand {
    position: absolute; left: 61px; top: 14px;
    display: flex; align-items: flex-start; gap: 4px;
    color: var(--paper);
    font-family: "Abel", sans-serif;
    font-size: 36px;
    line-height: 44px;
    letter-spacing: 2px;
  }
  .brand__dot {
    width: 8px; height: 8px; border-radius: 50%;
    border: 1.5px solid var(--paper);
    margin-top: 6px;
  }
  .header-rule {
    position: absolute; left: 81px; top: 64px;
    width: 553px; height: 3px;
    background: var(--brand-blue-dark);
    box-shadow: 0 1px 0 rgba(0,0,0,0.25);
  }
  .social-links {
    position: absolute; left: 427px; top: 37px;
    display: flex; gap: 38px;
  }
  .social-links__item {
    width: 18px; height: 18px; border-radius: 50%;
    background: var(--paper);
  }

  .slide__title {
    position: absolute; left: 42px; top: 101px;
    font-family: "Saira Condensed", sans-serif;
    font-weight: 700;
    font-size: 26px;
    line-height: 30px;
    letter-spacing: 0.5px;
    color: var(--ink);
    text-transform: uppercase;
    white-space: nowrap;
  }
  .slide__title-accent { color: var(--brand-blue); }

  .slide__body {
    position: absolute; left: 42px; top: 174px;
    width: 298px;
    font-size: 16px;
    line-height: 18.7px;
    letter-spacing: 0.3px;
    color: var(--body-text);
    text-align: justify;
  }
  .slide__body p + p { margin-top: 18.7px; }

  .photo { position: absolute; }
  .photo--team-circle {
    left: 376px; top: 169px; width: 307px; height: 242px;
    background: radial-gradient(ellipse at 55% 55%, #8fb6d6 0%, #c9d6e2 45%, #f3f3f3 75%, #ffffff 100%);
    border-radius: 40% 45% 8px 8px;
  }
  .photo--business-team {
    left: 372px; top: 204px; width: 295px; height: 187px;
    background: linear-gradient(90deg, #ffffff 0%, #6d7078 14%, #30333a 40%, #8a8d94 50%, #2a2b30 66%, #1c1d22 100%);
    border-radius: 6px;
  }

  .slide__footer {
    position: absolute; left: 0; bottom: 0;
    width: 100%; height: 41px;
    background: var(--footer-band);
  }
  .footer__url {
    position: absolute; left: 263px; top: 6px;
    width: 183px; height: 27px;
    background: var(--paper);
    border-radius: 4px;
    font-size: 16.5px;
    line-height: 27px;
    text-align: center;
    color: var(--ink);
  }
  .footer__page {
    position: absolute; left: 646px; top: 8px;
    width: 32px; height: 27px;
    background: var(--paper);
    font-size: 16px;
    line-height: 27px;
    text-align: center;
    color: var(--ink);
  }
  .slide--second .footer__page { left: 638px; }
</style>
</head>
<body>

<section class="slide slide--first">
  <header class="slide__header">
    <div class="brand">Vantora<span class="brand__dot"></span></div>
    <div class="social-links">
      <span class="social-links__item"></span>
      <span class="social-links__item"></span>
      <span class="social-links__item"></span>
      <span class="social-links__item"></span>
    </div>
    <div class="header-rule"></div>
  </header>
  <h1 class="slide__title">Your Pitcher <span class="slide__title-accent">Column Comes Here</span></h1>
  <div class="slide__body">
    <p>Based in Melbourne, Australia, Vantora is a management consulting organisation who partner with their clients to lead the execution of strategic process and system improvement initiatives. Our core purpose is to help your business navigate transformational change through clear and focused execution and enablement.</p>
    <p>Our Melbourne based office includes a range of professional management consulting services from business analysis, business intelligence, project management, business process management and change management.</p>
  </div>
  <div class="photo photo--team-circle" role="img" aria-label="Photo of a team stacking hands together in a circle, seen from above"></div>
  <footer class="slide__footer">
    <div class="footer__url">www.vantora.com.au</div>
    <div class="footer__page">07</div>
  </footer>
</section>

<section class="slide slide--second">
  <header class="slide__header">
    <div class="brand">Vantora<span class="brand__dot"></span></div>
    <div class="social-links">
      <span class="social-links__item"></span>
      <span class="social-links__item"></span>
      <span class="social-links__item"></span>
      <span class="social-links__item"></span>
    </div>
    <div class="header-rule"></div>
  </header>
  <h1 class="slide__title">Your Pitcher <span class="slide__title-accent">Column Comes Here</span></h1>
  <div class="slide__body">
    <p>Based in Melbourne, Australia, Vantora is a management consulting organisation who partner with their clients to lead the execution of strategic process and system improvement initiatives. Our core purpose is to help your business navigate transformational change through clear and focused execution and enablement.</p>
    <p>Our Melbourne based office includes a range of professional management consulting services from business analysis, business intelligence, project management, business process management and change management.</p>
  </div>
  <div class="photo photo--business-team" role="img" aria-label="Photo of a businesswoman in a dark suit in front of a blurred group of business colleagues"></div>
  <footer class="slide__footer">
    <div class="footer__url">www.vantora.com.au</div>
    <div class="footer__page">07</div>
  </footer>
</section>

</body>
</html>
```